Flyer for Quarry Lumina - Design Agency

We need a 4-page square flyer measuring 14.8x14.8cm per page, to fold out, for a design agency targeting small businesses.
The design should be very modern. There shouldn't be too much content visible.
The background should be black. The color of the logo (attached) can also be used. The content is also attached and divided per page. We are open to alternative suggestions regarding the division.

```html
<!DOCTYPE html>
<html lang="de">
<head>
<meta charset="utf-8">
<title>Quarry Lumina – Faltflyer</title>
<link rel="stylesheet" href="https://fonts.googleapis.com/css2?family=Figtree:ital,wght@0,300;0,400;0,500;0,600;0,700;1,600;1,700&display=swap">
<style>
  :root {
    --paper: #ffffff;
    --ink: #000000;
    --white: #ffffff;
    --teal: #a6dcdc;
    --blue: #1ba7dc;
    --magenta: #e6198a;
    --rule: #d9d9d9;
    --label: #222222;
  }
  * { margin: 0; padding: 0; box-sizing: border-box; }
  html, body { width: 1200px; height: 848px; overflow: hidden; background: var(--paper); }
  body { position: relative; font-family: "Figtree", sans-serif; color: var(--white); }

  .page-label {
    position: absolute; transform: translateX(-50%);
    font-family: "Figtree", sans-serif; font-weight: 300; font-size: 15px; color: var(--label);
  }

  .panel { position: absolute; background: var(--ink); overflow: hidden; }
  .panel--front { left: 36px; top: 52px; width: 362px; height: 361px; }
  .panel--inside { left: 416px; top: 52px; width: 361px; height: 722px; overflow: visible; }
  .panel--back { left: 795px; top: 52px; width: 362px; height: 361px; }

  .abs { position: absolute; }

  .brand-name { color: var(--teal); font-weight: 600; line-height: 0.92; letter-spacing: -0.5px; }
  .brand-name--large { left: 35px; top: 28px; font-size: 46px; }
  .brand-name--small { left: 25px; top: 208px; font-size: 17px; }
  .brand-name--back { left: 25px; top: 28px; font-size: 27px; }

  .front-claim { left: 36px; top: 296px; font-size: 13px; line-height: 15.6px; font-weight: 400; }
  .front-claim b { font-weight: 700; }
  .front-claim .c-white { color: var(--white); }
  .front-claim .c-teal { color: var(--teal); }
  .front-claim .c-blue { color: var(--blue); }

  .inside-lines { position: absolute; left: 0; top: 0; width: 361px; height: 722px; overflow: visible; }

  .headword { left: 26px; font-size: 31px; font-weight: 300; letter-spacing: 1px; line-height: 1; }
  .headword--modern { top: 40px; color: var(--white); }
  .headword--mutig { top: 77px; color: var(--teal); }
  .headword--markant { top: 112px; color: var(--blue); }

  .intro-mark { left: 104px; top: 216px; font-size: 10px; line-height: 13.6px; color: var(--teal); font-weight: 400; }
  .intro-text { left: 25px; top: 299px; font-size: 10.5px; line-height: 13.8px; color: var(--white); font-weight: 400; }

  .section-title { font-size: 11px; font-weight: 700; letter-spacing: 0.5px; color: var(--white); }
  .section-title--services { left: 25px; top: 373px; }
  .section-title--why { left: 27px; top: 629px; }

  .service { left: 22px; width: 300px; }
  .service__icon { position: absolute; left: 0; top: 2px; width: 26px; height: 26px; }
  .service__title { margin-left: 36px; font-size: 12px; font-weight: 500; color: var(--magenta); letter-spacing: 0.3px; line-height: 14px; }
  .service__text { margin-left: 36px; font-size: 8.5px; line-height: 10.4px; color: var(--teal); font-weight: 400; }
  .service--flyer { top: 396px; }
  .service--ci { top: 448px; }
  .service--digital { top: 505px; }
  .service--all { top: 562px; }

  .reasons { left: 26px; top: 643px; width: 300px; list-style: none; }
  .reasons li { position: relative; padding-left: 16px; font-size: 8.5px; line-height: 10.4px; color: var(--teal); margin-bottom: 2.6px; }
  .reasons li::before { content: ""; position: absolute; left: 2px; top: 1.5px; width: 3px; height: 3px; border-radius: 50%; background: var(--magenta); }

  .back-slogan { left: 25px; top: 96px; font-size: 16.5px; font-style: italic; font-weight: 700; line-height: 20.5px; color: var(--white); }
  .back-cta { left: 25px; top: 179px; font-size: 11px; line-height: 13.6px; color: var(--blue); font-weight: 400; letter-spacing: 0.3px; }
  .contact { left: 25px; top: 257px; font-size: 9.5px; line-height: 16px; color: var(--white); }
  .contact__address { color: var(--blue); line-height: 11.5px; margin-top: 1px; }
  .owners { left: 25px; top: 330px; font-size: 6.5px; color: var(--teal); }
</style>
</head>
<body>

  <span class="page-label" style="left:220px; top:29px;">front</span>
  <span class="page-label" style="left:601px; top:29px;">top</span>
  <span class="page-label" style="left:983px; top:29px;">back</span>
  <span class="page-label" style="left:604px; top:784px;">bottom</span>

  <!-- Front page -->
  <section class="panel panel--front">
    <div class="abs brand-name brand-name--large">Quarry<br>Lumina</div>
    <p class="abs front-claim">
      <span class="c-white">Dein <b>Unternehmen.</b></span><br>
      <span class="c-teal">Dein <b>Stil.</b></span><br>
      <span class="c-blue">Unser <b>Design.</b></span>
    </p>
  </section>

  <!-- Inside spread (top + bottom) -->
  <section class="panel panel--inside">
    <svg class="inside-lines" viewBox="0 0 361 722" fill="none" stroke-width="0.9">
      <polyline points="167,65 341,65 341,458 196,458" stroke="var(--rule)"/>
      <polyline points="130,101.5 306,101.5 306,405 178,405" stroke="var(--teal)"/>
      <polyline points="177,137 361,137" stroke="var(--blue)"/>
      <polyline points="159,515 346,515 346,722" stroke="var(--blue)"/>
      <polyline points="202,572 330,572 330,643 361,643" stroke="var(--magenta)"/>
    </svg>

    <h1 class="abs headword headword--modern">MODERN</h1>
    <h1 class="abs headword headword--mutig">MUTIG</h1>
    <h1 class="abs headword headword--markant">MARKANT</h1>

    <div class="abs brand-name brand-name--small">Quarry<br>Lumina</div>
    <p class="abs intro-mark">gestaltet die Zukunft deines<br>Unternehmensauftritts.</p>

    <p class="abs intro-text">Wir machen aus Ideen visuelle<br>Erlebnisse und sorgen dafür, dass<br>deine Marke im Gedächtnis bleibt.</p>

    <h2 class="abs section-title section-title--services">UNSERE LEISTUNGEN:</h2>

    <div class="abs service service--flyer">
      <svg class="service__icon" viewBox="0 0 26 26" fill="none" stroke="var(--white)" stroke-width="0.9" stroke-linejoin="round">
        <path d="M24 2 C16 3 9 9 6 16 L10 20 C17 17 23 10 24 2 Z"/>
        <circle cx="16" cy="10" r="1.5"/>
        <path d="M6 16 L2 15 L6 11 L10 11"/>
        <path d="M10 20 L11 24 L15 20 L15 16"/>
        <path d="M4 22 L7 19"/>
      </svg>
      <div class="service__title">NEXT-LEVEL FLYER</div>
      <div class="service__text">Nicht nur Papier, sondern deine Botschaft im<br>perfekten Look.</div>
    </div>

    <div class="abs service service--ci">
      <svg class="service__icon" viewBox="0 0 26 26" fill="none" stroke="var(--white)" stroke-width="0.9">
        <path d="M13 2 C6 2 2 7 2 13 C2 19 7 24 12 24 C14 24 14 22 13 20 C12 18 13 17 15 17 L18 17 C22 17 24 15 24 12 C24 6 19 2 13 2 Z"/>
        <circle cx="8" cy="9" r="1.6"/>
        <circle cx="13" cy="6.5" r="1.6"/>
        <circle cx="6.5" cy="15" r="1.6"/>
        <path d="M24 3 L15 13"/>
      </svg>
      <div class="service__title">CORPORATE IDENTITY</div>
      <div class="service__text">Ein Design, das deine Marke spricht – individuell,<br>stark, unvergesslich.</div>
    </div>

    <div class="abs service service--digital">
      <svg class="service__icon" viewBox="0 0 26 26" fill="none" stroke="var(--white)" stroke-width="0.9">
        <circle cx="13" cy="13" r="11"/>
        <ellipse cx="13" cy="13" rx="5" ry="11"/>
        <path d="M2 13 H24 M4 7.5 H22 M4 18.5 H22 M13 2 V24"/>
      </svg>
      <div class="service__title">DIGITAL &amp; PRINT</div>
      <div class="service__text">Ob Social Media Grafiken oder klassisches<br>Printdesign – wir sind da, wo du uns brauchst.</div>
    </div>

    <div class="abs service service--all">
      <svg class="service__icon" viewBox="0 0 26 26" fill="none" stroke="var(--white)" stroke-width="0.9" stroke-linejoin="round">
        <path d="M12 4 L14.3 9 L19.5 9.5 L15.5 13 L16.8 18 L12 15.3 L7.2 18 L8.5 13 L4.5 9.5 L9.7 9 Z"/>
        <path d="M18 16 L18 24 M18 20 C20 19 23 19 23 22 L22 25" />
        <path d="M2 4 L3 5 M22 3 L21 4 M2 20 L3 19"/>
      </svg>
      <div class="service__title">ALLES AUS EINER HAND</div>
      <div class="service__text">Logo, Farben, Typografie, Flyer und vieles mehr –<br>wir bauen das Fundament für deinen Erfolg.</div>
    </div>

    <h2 class="abs section-title section-title--why">WARUM WIR?</h2>
    <ul class="abs reasons">
      <li>Dein Style, unser Know-how: Wir kombinieren deine Vision<br>mit moderner Ästhetik.</li>
      <li>Persönlicher Service – Wir hören zu und setzen um, was<br>dich einzigartig macht</li>
      <li>Flexible Lösungen für die unterschiedlichsten Anforderungen</li>
    </ul>
  </section>

  <!-- Back page -->
  <section class="panel panel--back">
    <div class="abs brand-name brand-name--back">Quarry<br>Lumina</div>
    <p class="abs back-slogan">Designs, die wirken.<br>Marken, die bleiben.</p>
    <p class="abs back-cta">KONTAKTIERE UNS FÜR EINE<br>KOSTENLOSE BERATUNG!</p>
    <div class="abs contact">
      <div>design@quarrylumina.de</div>
      <div>+49 555 018204</div>
      <div class="contact__address">Lindenhofgasse 9<br>60311 Frankfurt</div>
    </div>
    <p class="abs owners">Inhaber: Lena Ostrow &amp; Tim Berger</p>
  </section>

</body>
</html>
```